New residential property management company

I have a lot of name recognition in our smaller town due to owning a construction company here. I have now started a residential property management company representing landlords and tenants. Just trying to get my name out there and get some rentals to manage!

```html
<!DOCTYPE html>
<html lang="en">
<head>
<meta charset="utf-8">
<title>Harlow Property Management – Postcard</title>
<link href="https://fonts.googleapis.com/css2?family=Oswald:wght@400;500&family=Open+Sans:wght@400;600;700&display=swap" rel="stylesheet">
<style>
  :root{
    --blue:#1f4e9c;
    --blue-deep:#173a80;
    --red:#b3262b;
    --ink:#1a1a1a;
    --grey-text:#555a60;
    --rule:#c9ccd1;
    --paper:#ffffff;
    --backdrop:#e6e7e9;
    --photo-warm-a:#c9a27a;
    --photo-warm-b:#e9e2d8;
    --photo-cool-a:#4a6a8e;
    --photo-cool-b:#cfd6de;
  }
  *{box-sizing:border-box;margin:0;padding:0}
  html,body{width:1016px;height:1200px;overflow:hidden;background:var(--backdrop)}
  body{position:relative;font-family:"Open Sans",Arial,sans-serif}
  ul{list-style:none}

  .card-slot{position:absolute;left:61px;width:893px;height:558px}
  .card-slot--front{top:28px}
  .card-slot--back{top:614px}
  .card{position:absolute;left:0;top:0;width:576px;height:360px;background:var(--paper);
        transform:scale(1.55);transform-origin:0 0;overflow:hidden;
        box-shadow:0 2px 6px rgba(0,0,0,.25)}
  .card__shapes{position:absolute;inset:0;width:576px;height:360px}
  .abs{position:absolute}

  .display{font-family:"Oswald",Arial,sans-serif;font-weight:500}

  /* brand */
  .brand{display:flex;align-items:center;gap:8px}
  .brand__mark{width:30px;height:30px;background:var(--ink)}
  .brand__text{font-family:"Oswald",Arial,sans-serif;font-weight:500;color:var(--ink);line-height:1}
  .brand__name{font-size:30px;letter-spacing:1px}
  .brand__sub{font-size:6.5px;letter-spacing:.6px;margin-top:3px}

  /* front */
  .front__kicker{left:14px;top:86px;font-size:18px;color:var(--blue);line-height:1}
  .front__title{left:14px;top:109px;font-size:23px;color:var(--blue);line-height:1;letter-spacing:.1px}
  .front__lede{left:14px;top:140px;width:232px;font-size:9.5px;color:var(--grey-text);line-height:1.3}
  .services{left:14px;top:187px;display:grid;grid-template-columns:128px 130px;row-gap:6px}
  .service{display:flex;align-items:center;gap:6px;font-family:"Open Sans",Arial,sans-serif;font-weight:600;font-size:9px;color:var(--ink);height:18px}
  .service svg{width:18px;height:18px;flex:none}

  .call{display:flex;align-items:center;gap:7px;color:#fff;font-family:"Oswald",Arial,sans-serif;font-size:19px;line-height:1;letter-spacing:.3px;white-space:nowrap}
  .call svg{width:14px;height:16px}
  .front__call{left:13px;top:307px}
  .web{font-size:9px;font-weight:700;color:var(--ink)}
  .front__web{left:16px;top:341px}

  .photo{position:absolute}

  /* back */
  .back__headline{left:17px;top:122px;font-size:13.8px;color:#fff;line-height:1;letter-spacing:.1px;white-space:nowrap}
  .back__sub{left:17px;top:141px;font-size:9px;color:#fff}
  .features{left:17px;top:166px;width:238px;display:flex;justify-content:space-between}
  .feature{width:72px;display:flex;flex-direction:column;align-items:center;gap:8px;color:#fff;font-family:"Open Sans",Arial,sans-serif;font-size:7px;font-weight:400}
  .feature svg{width:36px;height:30px}
  .about__label{left:17px;top:235px;font-size:13px;color:var(--blue);line-height:1}
  .about__body{left:17px;top:262px;width:249px;font-size:8.4px;line-height:1.42;color:#fff;text-align:justify}
  .stamp-box{left:490px;top:14px;width:72px;height:48px;border:1px solid var(--rule)}
  .address-line{left:315px;width:247px;height:1px;background:var(--rule)}
  .back__brand{left:320px;top:26px}
  .back__call{left:321px;top:310px}
  .back__web{left:422px;top:341px}
</style>
</head>
<body>

<!-- FRONT -->
<div class="card-slot card-slot--front">
  <section class="card card--front">
    <svg class="card__shapes" viewBox="0 0 576 360" aria-hidden="true">
      <defs>
        <linearGradient id="couplePhoto" x1="0" y1="0" x2="1" y2="1">
          <stop offset="0" stop-color="var(--photo-warm-b)"/>
          <stop offset=".5" stop-color="var(--photo-warm-a)"/>
          <stop offset="1" stop-color="var(--photo-cool-a)"/>
        </linearGradient>
      </defs>
      <polygon points="262,0 576,0 576,12 300,12 286,130 280,130" fill="var(--blue)"/>
      <polygon points="300,12 576,12 576,360 262,360 286,245 280,130" fill="url(#couplePhoto)"/>
      <polygon points="284,262 296,262 268,360 244,360" fill="var(--red)"/>
      <polygon points="0,300 290,300 276,336 0,336" fill="var(--blue)"/>
    </svg>
    <div class="photo" role="img" aria-label="Photo of a smiling young couple sitting on the floor among moving boxes in their new home" style="left:300px;top:12px;width:276px;height:348px"></div>

    <div class="abs brand" style="left:14px;top:20px">
      <span class="brand__mark"></span>
      <div class="brand__text">
        <div class="brand__name">HARLOW</div>
        <div class="brand__sub">PROPERTY MANAGEMENT LLC.</div>
      </div>
    </div>

    <div class="abs display front__kicker">FULL-SERVICE</div>
    <h1 class="abs display front__title">PROPERTY MANAGEMENT</h1>
    <p class="abs front__lede">Maximize your financial returns with support from our rental specialists</p>

    <ul class="abs services">
      <li class="service"><svg viewBox="0 0 18 18"><circle cx="9" cy="9" r="9" fill="var(--blue)"/><circle cx="7" cy="7" r="2" fill="#fff"/><circle cx="11.5" cy="7" r="2" fill="#fff"/><path d="M3.5 13a3.5 3 0 0 1 7 0zM8 13a3.5 3 0 0 1 7 0z" fill="#fff"/></svg>TENAT SCREENING</li>
      <li class="service"><svg viewBox="0 0 18 18"><circle cx="9" cy="9" r="9" fill="var(--blue)"/><rect x="4.5" y="5" width="9" height="8" rx="1" fill="#fff"/><rect x="6" y="7" width="6" height="1.2" fill="var(--blue)"/><rect x="6" y="9.5" width="4" height="1.2" fill="var(--blue)"/></svg>MANAGEMENT</li>
      <li class="service"><svg viewBox="0 0 18 18"><circle cx="9" cy="9" r="9" fill="var(--blue)"/><path d="M9 4l4 1.5v3c0 2.5-1.8 4.3-4 5-2.2-.7-4-2.5-4-5v-3z" fill="#fff"/></svg>RENT COLLECTION</li>
      <li class="service"><svg viewBox="0 0 18 18"><circle cx="9" cy="9" r="9" fill="var(--blue)"/><rect x="5" y="4" width="8" height="10" rx="1" fill="#fff"/><rect x="6.5" y="6" width="5" height="1" fill="var(--blue)"/><rect x="6.5" y="8.3" width="5" height="1" fill="var(--blue)"/><rect x="6.5" y="10.6" width="5" height="1" fill="var(--blue)"/></svg>ACCOUNTING</li>
      <li class="service"><svg viewBox="0 0 18 18"><circle cx="9" cy="9" r="9" fill="var(--blue)"/><path d="M5 5l8 8M13 5l-8 8" stroke="#fff" stroke-width="2" stroke-linecap="round"/></svg>MAINTENANCE</li>
      <li class="service"><svg viewBox="0 0 18 18"><circle cx="9" cy="9" r="9" fill="var(--blue)"/><path d="M9 4l5 4.5h-1.5V13h-7V8.5H4z" fill="#fff"/></svg>HOA COMPLANCE</li>
      <li class="service"><svg viewBox="0 0 18 18"><circle cx="9" cy="9" r="9" fill="var(--blue)"/><circle cx="9" cy="6.5" r="2.2" fill="none" stroke="#fff" stroke-width="1.4"/><path d="M9 8.7V14M9 11.5h2M9 13.3h2" stroke="#fff" stroke-width="1.4"/></svg>LEASING</li>
      <li class="service"><svg viewBox="0 0 18 18"><circle cx="9" cy="9" r="9" fill="var(--blue)"/><circle cx="9" cy="7.5" r="2.5" fill="#fff"/><path d="M4.5 14a4.5 3.5 0 0 1 9 0z" fill="#fff"/><path d="M5.5 8a3.5 3.5 0 0 1 7 0" stroke="#fff" fill="none"/></svg>24/7 SUPPORT</li>
    </ul>

    <div class="abs call front__call">CALL US NOW
      <svg viewBox="0 0 14 16" aria-hidden="true"><rect x="2" y="0.5" width="10" height="15" rx="2" fill="#fff"/><rect x="3.8" y="2.5" width="6.4" height="9" fill="var(--blue)"/><circle cx="7" cy="13.5" r="1" fill="var(--blue)"/></svg>
      (555) 284-7190</div>
    <div class="abs web front__web">www.harlowmanagement.com</div>
  </section>
</div>

<!-- BACK -->
<div class="card-slot card-slot--back">
  <section class="card card--back">
    <svg class="card__shapes" viewBox="0 0 576 360" aria-hidden="true">
      <defs>
        <linearGradient id="housePhoto" x1="0" y1="0" x2="1" y2="1">
          <stop offset="0" stop-color="var(--photo-cool-b)"/>
          <stop offset=".6" stop-color="#eef0f2"/>
          <stop offset="1" stop-color="var(--photo-cool-a)"/>
        </linearGradient>
        <linearGradient id="aboutBlue" x1="0" y1="0" x2="1" y2="1">
          <stop offset="0" stop-color="var(--blue-deep)"/>
          <stop offset="1" stop-color="var(--blue)"/>
        </linearGradient>
      </defs>
      <rect x="0" y="0" width="272" height="112" fill="url(#housePhoto)"/>
      <rect x="0" y="112" width="272" height="126" fill="var(--red)"/>
      <polygon points="0,238 272,238 312,330 312,360 0,360" fill="url(#aboutBlue)"/>
      <polygon points="0,230 128,230 136,252 0,252" fill="#fff"/>
      <polygon points="466,298 576,298 576,306 462,306" fill="var(--blue)"/>
      <polygon points="308,306 576,306 576,338 300,338" fill="var(--red)"/>
    </svg>
    <div class="photo" role="img" aria-label="Photo of two hands cupped around a small model house on a desk" style="left:0;top:0;width:272px;height:112px"></div>

    <h2 class="abs display back__headline">YOUR HOME. YOUR PROJECTS. SIMPLIFIED.</h2>
    <p class="abs back__sub">We serve landlords and tenants</p>

    <ul class="abs features">
      <li class="feature"><svg viewBox="0 0 36 30"><path d="M18 2L34 15H29V28H7V15H2z" fill="#fff"/></svg>PROPERTIES</li>
      <li class="feature"><svg viewBox="0 0 36 30"><path d="M8 3l22 22" stroke="#fff" stroke-width="5"/><path d="M29 3L7 25" stroke="#fff" stroke-width="5"/><path d="M5 28l2-5 3 3z" fill="#fff"/></svg>PROJECTS</li>
      <li class="feature"><svg viewBox="0 0 36 30"><circle cx="18" cy="9" r="5" fill="#fff"/><circle cx="7" cy="12" r="4" fill="#fff"/><circle cx="29" cy="12" r="4" fill="#fff"/><path d="M10 28a8 8 0 0 1 16 0zM0 28a7 7 0 0 1 12-5v5zM36 28a7 7 0 0 0-12-5v5z" fill="#fff"/></svg>PARTNERS</li>
    </ul>

    <div class="abs display about__label">ABOUT US</div>
    <p class="abs about__body">Our standardized full-service property management program is specifically designed for owners who want to enjoy the benefits of home ownership, but do not want the hassle of dealing with all of the day-to-day demands required to successfully manage the hassle of it all. Why worry about managing your estate, let a property management professional do it.</p>

    <div class="abs brand back__brand">
      <span class="brand__mark" style="width:24px;height:24px"></span>
      <div class="brand__text">
        <div class="brand__name" style="font-size:24px">HARLOW</div>
        <div class="brand__sub" style="font-size:5.2px">PROPERTY MANAGEMENT LLC.</div>
      </div>
    </div>
    <div class="abs stamp-box"></div>
    <div class="abs address-line" style="top:122px"></div>
    <div class="abs address-line" style="top:152px"></div>
    <div class="abs address-line" style="top:182px"></div>
    <div class="abs address-line" style="top:213px"></div>

    <div class="abs call back__call">CALL US NOW
      <svg viewBox="0 0 14 16" aria-hidden="true"><rect x="2" y="0.5" width="10" height="15" rx="2" fill="#fff"/><rect x="3.8" y="2.5" width="6.4" height="9" fill="var(--red)"/><circle cx="7" cy="13.5" r="1" fill="var(--red)"/></svg>
      (555) 284-7190</div>
    <div class="abs web back__web">www.harlowmanagement.com</div>
  </section>
</div>

</body>
</html>
```